Wix Design for a Clothing Design Web Marketing Site

We need a Wix design and content (including any images and copy) for a clothing design web storefront, Made 4 Me Now (or made4menow). Rough ideas and content can be found at http://marenoltsby.example-site.com/made4menow.

Made For Me Now is an innovative business concept that combines fashion and entertainment. The business model allows customers to actively participate in the creation of fashion designs/concepts , visualize the garment in the customer’s body in 3D, and buy the physical garment made specially to fit the customer.
The fashion consultant will be able to create the design based on client's desires and test various possibilities (size, fabric, cut, etc..) in front of the customer, using software Venlora (the software is a key component of this business model)
(when developing the website use images from Venlora)
After the design is created, the customer can choose to order the actual piece. The garment will be made according to the created design, the customer measurements.

Target Market(s)

Primarily women from 25 to 45, who are fashion enthusiasts and appreciate fit and exclusivity. They are hedonistic shoppers, who shop for entertainment.
Men (metrosexuals) who are fashion enthusiasts, also hedonistic shoppers.

Industry/Entity Type

Clothing

Font styles to use
Serif
Sans Serif

Requirements
Must have
• Must have a landing page (home) or section, that gives the consumer an idea of what Made 4 Me Now will do for them, an about page or section that tells about the company and product, a how it works page or section that describes how it works (http://marenoltsby.example-site.com/made4menow#!services3/c192y), and page or section about pricing, and a page or section on how to contact us.
Nice to have
• Very modern and clean. The website must be based on the main picture of the studio in the example. If that studio is the store, what will the website look like?
• Colors yellow, grey and white. Use the zig zag in yellow and white. You can change the size of the lines. The zig zagi gives the modern and bold accent. Outfits in pictures must show nicely tailored garments.

```html
<!DOCTYPE html>
<html lang="en">
<head>
<meta charset="utf-8">
<title>Made For Me Now — Home</title>
<link rel="stylesheet" href="https://fonts.googleapis.com/css2?family=Archivo+Black&family=Barlow:wght@300;400&family=Libre+Baskerville:ital@1&display=swap">
<style>
  :root {
    --white: #ffffff;
    --page-grey: #e4e4e2;
    --ink: #3c3c3c;
    --ink-soft: #5a5a5a;
    --nav-rule: #9a9a9a;
    --nav-rule-active: #5b5b5b;
    --yellow: #fcc800;
    --photo-light: #e6e6e4;
    --photo-mid: #d9d6d1;
    --photo-warm: #d8cdc2;
  }
  * { box-sizing: border-box; margin: 0; padding: 0; }
  html, body { width: 1200px; height: 618px; overflow: hidden; background: var(--page-grey); }
  .canvas { position: relative; width: 1200px; height: 618px; overflow: hidden; font-family: "Barlow", sans-serif; color: var(--ink); }

  .site-header { position: absolute; left: 0; top: 0; width: 1200px; height: 101px; background: var(--white); z-index: 2; }
  .brand { position: absolute; left: 165px; top: 30px; display: flex; align-items: center; gap: 6px; z-index: 3; }
  .brand-mark { width: 10px; height: 10px; background: var(--yellow); }
  .brand-name { font-family: "Barlow", sans-serif; font-weight: 400; font-size: 14px; color: var(--ink); letter-spacing: 0.3px; }
  .tagline { position: absolute; left: 305px; top: 81px; font-family: "Libre Baskerville", serif; font-style: italic; font-size: 10px; color: var(--ink); }

  .main-nav { position: absolute; left: 488px; top: 25px; display: flex; gap: 7px; }
  .nav-item { width: 100px; border-top: 1px solid var(--nav-rule); padding-top: 9px; text-align: center; font-size: 13px; font-weight: 400; letter-spacing: 0.6px; color: var(--ink-soft); }
  .nav-item.is-active { border-top: 3px solid var(--nav-rule-active); padding-top: 7px; }

  .hero-photo { position: absolute; left: 0; top: 101px; width: 1200px; height: 517px;
    background: linear-gradient(90deg, var(--photo-mid) 0%, var(--photo-light) 45%, var(--photo-warm) 80%, var(--photo-light) 100%); }

  .philosophy-panel { position: absolute; left: 163px; top: 152px; width: 193px; height: 480px; background: var(--white); padding: 42px 30px 0 11px; }
  .panel-title { font-size: 20px; font-weight: 300; letter-spacing: 0.5px; color: var(--ink); line-height: 24px; }
  .panel-rule { width: 28px; height: 2px; background: var(--ink); margin: 14px 0 16px; }
  .pillar { margin-bottom: 16px; }
  .pillar-title { font-size: 13px; font-weight: 400; letter-spacing: 0.3px; line-height: 16px; }
  .pillar-text { font-size: 12px; font-weight: 300; line-height: 15.8px; color: var(--ink-soft); letter-spacing: 0.2px; }

  .hero-frame { position: absolute; left: 378px; top: 152px; width: 643px; height: 520px; border: 10px solid var(--yellow); }
  .hero-headline { position: absolute; left: 421px; top: 200px; font-family: "Archivo Black", sans-serif; font-size: 60px; line-height: 56px; color: var(--yellow); text-transform: uppercase; letter-spacing: -0.5px; }
</style>
</head>
<body>
<div class="canvas">
  <div class="hero-photo" role="img" aria-label="Photo of two children in soft onesies playing in a bright white room"></div>

  <header class="site-header">
    <nav class="main-nav">
      <div class="nav-item is-active">HOME</div>
      <div class="nav-item">WHAT WE DO</div>
      <div class="nav-item">HOW IT WORKS</div>
      <div class="nav-item">PRICING</div>
      <div class="nav-item">CONTACT US</div>
    </nav>
    <p class="tagline">Clothes made specially for you and designed by you.</p>
  </header>

  <div class="brand">
    <span class="brand-mark"></span>
    <span class="brand-name">Made For Me Now</span>
  </div>

  <aside class="philosophy-panel">
    <h2 class="panel-title">Philopsophy</h2>
    <div class="panel-rule"></div>
    <div class="pillar">
      <h3 class="pillar-title">INSPIRATION</h3>
      <p class="pillar-text">Be inspired by the latest trend, iconic styles from all eras and the most prestigious fashion shows.</p>
    </div>
    <div class="pillar">
      <h3 class="pillar-title">DESIGN</h3>
      <p class="pillar-text">Learn about our unique process, where YOU become the designer.</p>
    </div>
    <div class="pillar">
      <h3 class="pillar-title">FREEDOM</h3>
      <p class="pillar-text">Choose from first rate fabrics &amp; highest quality materials.</p>
    </div>
    <div class="pillar">
      <h3 class="pillar-title">SEE</h3>
      <p class="pillar-text">See your creations in 3D.</p>
    </div>
  </aside>

  <div class="hero-frame"></div>
  <h1 class="hero-headline">A little<br>imagination<br>makes<br>clothes<br>come alive.</h1>
</div>
</body>
</html>
```